Update existing website to a one page design.

Combine a multi page website into a single page design.
Existing site is at ac.tallowmerecover (dot) com.
Rearrange elements as needed to create a modem look.
Not every element / all of the text need to be kept, design should be flexible enough to allow for new text (of different length) to be used.
Site should have a clear calls to action, such as get a quote and contact us.
Ability, call to action, to switch to Russian should be clearly visible near the top, translation will not be done by vextra, thus attribution is not needed.
Unused features (such as blog) should be dropped.
Images, besides logos, can be brand new.
Site should adhere to standard design practices (such as grid) and ideally be compatible with existing framework (such as bootstrap).
Coding of the website will likely be done by the winning bidder as a separate project.

```html
<!DOCTYPE html>
<html lang="en">
<head>
<meta charset="utf-8">
<title>Tallowmere Cover – Insurance</title>
<link rel="stylesheet" href="https://fonts.googleapis.com/css2?family=Heebo:wght@400;500;700&family=Josefin+Sans:wght@400;500;600&display=swap">
<style>
:root{
  --navy:#1e3f8f;
  --navy-dark:#1a3784;
  --orange:#ef6a25;
  --ink:#2b2b2b;
  --muted:#555b66;
  --pale:#eef2f8;
  --wave:#8a9fc9;
  --white:#ffffff;
  --line:#d9dee8;
}
*{box-sizing:border-box;margin:0;padding:0}
html,body{width:1200px;height:2317px;overflow:hidden;background:var(--white)}
body{font-family:"Josefin Sans",sans-serif;color:var(--ink);position:relative}
.abs{position:absolute}

/* buttons */
.pill{position:absolute;display:flex;align-items:center;justify-content:space-between;border-radius:18px;font-family:"Heebo",sans-serif;font-weight:500;font-size:9px;letter-spacing:.4px;color:var(--white);padding:0 4px 0 20px;text-transform:uppercase}
.pill .arrow{width:21px;height:21px;border-radius:50%;background:var(--white);display:flex;align-items:center;justify-content:center}
.pill--navy{background:var(--navy)}
.pill--orange{background:var(--orange)}

/* header */
.brand{position:absolute;left:102px;top:21px;width:86px;height:86px;background:var(--navy);border:3px solid var(--white);outline:1px solid var(--navy);display:flex;align-items:center;justify-content:center;text-align:center;z-index:3;overflow:hidden}
.brand span{font-family:"Josefin Sans",sans-serif;font-weight:600;font-size:10px;line-height:1.25;color:var(--white);letter-spacing:0}
.topbar-phone{left:671px;top:21px;font-family:"Heebo",sans-serif;font-size:13px;color:var(--navy)}
.social{left:800px;top:12px;width:31px;height:31px;border-radius:50%;background:var(--navy)}
.lang{position:absolute;left:1019px;top:12px;width:81px;height:31px;border-radius:16px;background:var(--navy);color:var(--white);font-family:"Heebo",sans-serif;font-size:9px;font-weight:500;display:flex;align-items:center;justify-content:space-between;padding:0 5px 0 23px}
.lang .arrow{width:21px;height:21px;border-radius:50%;background:var(--white);display:flex;align-items:center;justify-content:center}
.nav{left:308px;top:63px;width:793px;display:flex;justify-content:space-between;font-family:"Heebo",sans-serif;font-size:8.4px;font-weight:500;color:#222;letter-spacing:.2px}
.nav .current{color:var(--navy)}

/* hero */
.hero{left:0;top:94px;width:1200px;height:473px;background:linear-gradient(100deg,#4c4a44 0%,#6d6a62 35%,#8e8a80 60%,#6e6c68 100%)}
.hero-shade{left:0;top:94px;width:1200px;height:473px;background:linear-gradient(90deg,rgba(20,24,36,.55),rgba(20,24,36,.15) 70%)}
.hero-kicker{left:100px;top:182px;font-family:"Heebo",sans-serif;font-weight:700;font-size:21px;color:var(--orange)}
.hero-title{left:100px;top:222px;width:550px;font-family:"Josefin Sans",sans-serif;font-weight:500;font-size:29.5px;line-height:36px;color:var(--white)}
.quote-accent{left:913px;top:126px;width:206px;height:243px;background:var(--orange)}
.quote-panel{left:832px;top:144px;width:268px;height:306px;background:var(--navy);padding:14px 19px}
.quote-panel h2{font-family:"Heebo",sans-serif;font-weight:700;font-size:22px;line-height:27px;text-align:center;color:var(--white);margin-bottom:11px}
.field{height:31px;background:var(--white);margin-bottom:12.5px;font-size:9.5px;color:var(--navy);display:flex;align-items:center;justify-content:space-between;padding:0 12px}
.quote-panel .pill{position:relative;height:31px;justify-content:center;padding:0;margin-top:1px}

/* about */
.about-accent{left:369px;top:797px;width:143px;height:206px;background:var(--orange)}
.about-photo{left:200px;top:628px;width:293px;height:357px;border-radius:0 0 0 34px;background:linear-gradient(160deg,#e9e6e0 0%,#c9c3b8 45%,#8a8f9c 100%)}
.eyebrow{font-family:"Heebo",sans-serif;font-size:10px;color:var(--navy);text-transform:uppercase}
.section-title{font-family:"Heebo",sans-serif;font-weight:500;font-size:24px;color:var(--orange);text-transform:uppercase;letter-spacing:.2px}
.about-text{left:613px;top:662px;width:387px}
.about-text .section-title{margin-top:4px}
.about-text .rule{width:62px;height:1.5px;background:var(--navy);margin:6px 0 16px}
.about-text p{font-size:11px;line-height:15px;color:var(--muted);text-align:justify;margin-bottom:15px}

/* services */
.services-title{left:0;width:1200px;text-align:center}
.tabs{left:93px;top:1230px;width:1014px;display:flex}
.tab{flex:1;height:131px;display:flex;flex-direction:column;align-items:center;padding-top:26px;border-right:1px solid #dfe4ee;font-size:12.6px;color:var(--navy);text-align:center;line-height:15px;position:relative}
.tab:last-child{border-right:none}
.tab svg{margin-bottom:10px}
.tab--active{background:var(--navy);color:var(--white);border-right:none}
.tab--active::after{content:"";position:absolute;bottom:-8px;left:50%;margin-left:-8px;border-left:8px solid transparent;border-right:8px solid transparent;border-top:8px solid var(--navy)}
.panel{left:0;top:1406px;width:1200px;text-align:center}
.panel h3{font-family:"Josefin Sans",sans-serif;font-weight:500;font-size:21px;color:var(--navy);margin-bottom:11px}
.panel p{font-size:11.2px;line-height:15px;color:#222}

/* carriers */
.carriers{left:212px;top:1762px;display:flex;gap:13px}
.carrier{width:119px;height:61px;border:1px solid var(--line);background:var(--white);display:flex;align-items:center;justify-content:center;font-family:"Josefin Sans",sans-serif;font-weight:600;font-size:11.5px;color:var(--navy);text-align:center;line-height:13px;padding:0 6px}

/* footer */
.footer{left:0;top:1949px;width:1200px;height:368px;background:var(--navy);color:var(--white)}
.footer .brand{left:201px;top:76px;width:89px;height:89px;outline:none}
.fcol{position:absolute;top:75px}
.fcol h4{font-family:"Josefin Sans",sans-serif;font-weight:500;font-size:12px;margin-bottom:19px}
.fcol .small{font-size:8.8px;line-height:15px}
.fcol .list div{font-size:8.8px;margin-bottom:13.5px}
.f-call{font-size:12.6px;margin-bottom:3px}
.email-field{width:181px;height:31px;border-radius:16px;background:#9aa9d0;color:var(--navy);font-size:8.5px;display:flex;align-items:center;padding-left:12px;margin:12px 0 13px}
.send{position:relative;width:76px;height:31px;border-radius:16px;background:var(--white);color:var(--navy);font-family:"Heebo",sans-serif;font-size:8.5px;font-weight:500;display:flex;align-items:center;justify-content:space-between;padding:0 5px 0 20px}
.send .arrow{width:19px;height:19px;border-radius:50%;background:var(--navy);display:flex;align-items:center;justify-content:center}
.f-rule{left:131px;top:298px;width:938px;height:1px;background:#3e5ca5}
.copy{left:0;top:329px;width:1200px;text-align:center;font-size:8.8px}
</style>
</head>
<body>

<!-- header -->
<div class="brand"><span>TALLOWMERE<br>COVER</span></div>
<div class="abs topbar-phone">Call. 800-555-0142</div>
<div class="abs social" aria-label="Social link"></div>
<div class="pill pill--orange" style="left:844px;top:12px;width:162px;height:31px">Get an instant quote<span class="arrow"><svg width="10" height="10" viewBox="0 0 10 10"><path d="M1 5h7M5 2l3 3-3 3" stroke="#ef6a25" stroke-width="1.3" fill="none"/></svg></span></div>
<div class="lang">ENG<span class="arrow"><svg width="10" height="10" viewBox="0 0 10 10"><path d="M2 4l3 3 3-3" stroke="#1e3f8f" stroke-width="1.3" fill="none"/></svg></span></div>
<nav class="abs nav">
  <span class="current">HOME</span><span>ABOUT</span><span>INDIVIDUAL HEALTH</span><span>GROUP HEALTH</span><span>LIFE INSURANCE</span><span>PENSION &amp; ANNUITIES</span><span>PROPERTY &amp; COMMERCIAL</span><span>DOCTORS NETWORK</span><span>CONTACT</span>
</nav>

<!-- hero -->
<div class="abs hero" role="img" aria-label="Photo of a smiling family playing together on a sofa in a bright living room"></div>
<div class="abs hero-shade"></div>
<svg class="abs" style="left:0;top:480px" width="1200" height="90" viewBox="0 0 1200 90" preserveAspectRatio="none">
  <path d="M0 12 C160 20 300 80 470 86 C650 92 820 50 980 42 C1080 38 1150 50 1200 62 L1200 90 L0 90 Z" fill="#fff"/>
</svg>
<div class="abs hero-kicker">TALLOWMERE COVER</div>
<h1 class="abs hero-title">We Offer Insurance Coverage for Health, Life, Long Term Care, Disability Income, Mortgage Protection and Home Owners Plans</h1>
<div class="pill pill--navy" style="left:100px;top:391px;width:156px;height:30px">Contact us today!<span class="arrow"><svg width="10" height="10" viewBox="0 0 10 10"><path d="M1 5h7M5 2l3 3-3 3" stroke="#1e3f8f" stroke-width="1.3" fill="none"/></svg></span></div>

<div class="abs quote-accent"></div>
<form class="abs quote-panel">
  <h2>GET AN INSTANT QUOTE</h2>
  <div class="field">Name</div>
  <div class="field">Phone</div>
  <div class="field">Email</div>
  <div class="field">Select Your Carriers<svg width="10" height="10" viewBox="0 0 10 10"><path d="M2 4l3 3 3-3" stroke="#1e3f8f" stroke-width="1" fill="none"/></svg></div>
  <div class="pill pill--orange">Get a quote</div>
</form>

<!-- about -->
<div class="abs about-accent"></div>
<div class="abs about-photo" role="img" aria-label="Photo of parents making a roof with their arms over two children at home"></div>
<div class="abs about-text">
  <div class="eyebrow">Welcome to</div>
  <div class="section-title">Tallowmere Cover</div>
  <div class="rule"></div>
  <p>Tallowmere Cover Corporation is an Independent Insurance and Financial Brokerage Firm serving clients throughout Florida and Internationally. We are an experienced team of professionals, committed to our primary mission – to find the less expensive insurance coverage, for protection you want, at the best rate you deserve. Our integrated suite of online services facilitates a comprehensive search and review of leading insurance companies.</p>
  <p>Tallowmere Cover Corporation is not owned by any insurance company, therefore we provide objective information to consumers and small business owners, helping them make ...</p>
</div>
<div class="pill pill--navy" style="left:613px;top:917px;width:105px;height:31px">About us<span class="arrow"><svg width="10" height="10" viewBox="0 0 10 10"><path d="M1 5h7M5 2l3 3-3 3" stroke="#1e3f8f" stroke-width="1.3" fill="none"/></svg></span></div>

<!-- services band -->
<svg class="abs" style="left:0;top:1060px" width="1200" height="580" viewBox="0 0 1200 580" preserveAspectRatio="none">
  <path d="M0 14 C300 0 520 40 720 40 C900 40 1050 0 1200 4 L1200 560 C1000 560 800 560 600 548 C400 536 200 520 0 566 Z" fill="#eef2f8"/>
  <path d="M500 22 C700 -4 860 36 1000 36 C1100 36 1160 20 1200 6 L1200 36 C1100 50 1000 56 860 52 C740 48 640 30 500 22 Z" fill="#8a9fc9"/>
  <path d="M0 530 C180 500 360 510 520 526 C600 534 660 540 700 544 C560 544 420 522 260 532 C160 538 80 560 0 568 Z" fill="#8a9fc9"/>
</svg>
<div class="abs services-title" style="top:1160px"><div class="eyebrow">What we do</div></div>
<div class="abs services-title section-title" style="top:1176px">Insurance services we offer</div>

<div class="abs tabs">
  <div class="tab"><svg width="50" height="48" viewBox="0 0 50 48"><path d="M25 46 C10 34 0 25 0 14 A12 12 0 0 1 25 8 A12 12 0 0 1 50 14 C50 25 40 34 25 46Z" fill="#ef6a25"/><path d="M22 14h6v7h7v6h-7v7h-6v-7h-7v-6h7z" fill="#fff"/></svg>Individual Health</div>
  <div class="tab"><svg width="70" height="48" viewBox="0 0 70 48"><circle cx="14" cy="12" r="6" fill="#ef6a25"/><circle cx="56" cy="12" r="6" fill="#ef6a25"/><circle cx="35" cy="8" r="7" fill="#ef6a25"/><rect x="3" y="20" width="20" height="26" rx="5" fill="#ef6a25"/><rect x="47" y="20" width="20" height="26" rx="5" fill="#ef6a25"/><rect x="22" y="18" width="26" height="30" rx="6" fill="#ef6a25"/><path d="M33 26h4v5h5v4h-5v5h-4v-5h-5v-4h5z" fill="#fff"/></svg>Group Health</div>
  <div class="tab tab--active"><svg width="50" height="50" viewBox="0 0 50 50"><path d="M25 26 C16 19 12 15 12 10 A6 6 0 0 1 25 7 A6 6 0 0 1 38 10 C38 15 34 19 25 26Z" fill="#ef6a25"/><path d="M23 9h4v4h4v4h-4v4h-4v-4h-4v-4h4z" fill="#fff"/><path d="M2 18 L8 32 L18 40 L18 50 L24 50 L24 38 L14 28 L10 18Z" fill="#ef6a25"/><path d="M48 18 L42 32 L32 40 L32 50 L26 50 L26 38 L36 28 L40 18Z" fill="#ef6a25"/></svg>Life Insurance</div>
  <div class="tab"><svg width="50" height="50" viewBox="0 0 50 50"><circle cx="22" cy="11" r="10" fill="#ef6a25"/><text x="22" y="16" font-size="13" font-family="Heebo,sans-serif" font-weight="700" fill="#fff" text-anchor="middle">$</text><path d="M14 24h16v14H14z" fill="#ef6a25"/><path d="M6 44 C16 48 34 48 46 40" stroke="#ef6a25" stroke-width="3" fill="none"/><path d="M12 38v8M34 38v8" stroke="#ef6a25" stroke-width="3"/></svg>Pension &amp; Annuities</div>
  <div class="tab"><svg width="50" height="50" viewBox="0 0 50 50"><rect x="6" y="4" width="20" height="46" fill="#ef6a25"/><rect x="26" y="18" width="20" height="32" fill="#ef6a25"/><g fill="#fff"><rect x="10" y="10" width="4" height="4"/><rect x="18" y="10" width="4" height="4"/><rect x="10" y="20" width="4" height="4"/><rect x="18" y="20" width="4" height="4"/><rect x="10" y="30" width="4" height="4"/><rect x="18" y="30" width="4" height="4"/><rect x="30" y="24" width="4" height="4"/><rect x="38" y="24" width="4" height="4"/><rect x="30" y="34" width="4" height="4"/><rect x="38" y="34" width="4" height="4"/><rect x="13" y="41" width="6" height="9"/></g></svg>Property and<br>Commercial</div>
  <div class="tab"><svg width="50" height="50" viewBox="0 0 50 50"><rect x="15" y="0" width="20" height="10" rx="3" fill="#ef6a25"/><path d="M23 2h4v2h2v3h-2v2h-4V7h-2V4h2z" fill="#fff"/><circle cx="25" cy="17" r="8" fill="#ef6a25"/><path d="M4 50 C4 36 12 28 25 28 C38 28 46 36 46 50Z" fill="#ef6a25"/><circle cx="17" cy="42" r="3" fill="#fff"/><circle cx="33" cy="42" r="3" fill="#fff"/></svg>Doctors Network</div>
</div>

<div class="abs panel">
  <h3>Life Insurance</h3>
  <p>We are specialists in all types of Life Insurance in all of Florida and even internationally.<br>Consider these safety net vehicles as a vital piece of your long-term insurance strategy and estate planning.<br>We will find the options that are the best fits for you from which to choose:</p>
</div>
<div class="pill pill--orange" style="left:547px;top:1508px;width:106px;height:31px">Read more<span class="arrow"><svg width="10" height="10" viewBox="0 0 10 10"><path d="M1 5h7M5 2l3 3-3 3" stroke="#ef6a25" stroke-width="1.3" fill="none"/></svg></span></div>

<!-- carriers -->
<div class="abs services-title" style="top:1691px"><div class="eyebrow">Apply directly to</div></div>
<div class="abs services-title section-title" style="top:1707px">Your preferred carrier</div>
<div class="abs carriers">
  <div class="carrier">Northgate Mutual</div>
  <div class="carrier">Meridian Care</div>
  <div class="carrier">Crestline</div>
  <div class="carrier">Atlas Medical Group</div>
  <div class="carrier">Harborview</div>
  <div class="carrier">Beacon Shield</div>
</div>
<div class="pill pill--navy" style="left:519px;top:1856px;width:162px;height:31px">Get an instant quote<span class="arrow"><svg width="10" height="10" viewBox="0 0 10 10"><path d="M1 5h7M5 2l3 3-3 3" stroke="#1e3f8f" stroke-width="1.3" fill="none"/></svg></span></div>

<!-- footer -->
<footer class="abs footer">
  <div class="brand"><span>TALLOWMERE<br>COVER</span></div>
  <div class="fcol" style="left:406px">
    <h4>Need Help?</h4>
    <div class="f-call">Call:&nbsp; 800-555-0142</div>
    <div class="small">E: info@tallowmerecover.com</div>
    <div class="small" style="margin-top:8px;font-weight:600">Address:</div>
    <div class="small">410 Harbor Lane – Suite 12<br>Palmetto Bay, FL 33100</div>
    <div style="width:31px;height:31px;border-radius:50%;background:var(--orange);margin-top:18px" aria-label="Social link"></div>
  </div>
  <div class="fcol" style="left:613px">
    <h4>Our Services</h4>
    <div class="list"><div>Individual Health</div><div>Group Health</div><div>Life Insurance</div><div>Pension &amp; Annuities</div><div>Property &amp; Commercial</div><div>Doctors Network</div></div>
  </div>
  <div class="fcol" style="left:819px">
    <h4>Subscribe Now!</h4>
    <div class="small" style="line-height:12px">You Want to get Update<br>about anything News? Join Me Now!</div>
    <div class="email-field">Enter Your Email ...</div>
    <div class="send">SEND<span class="arrow"><svg width="9" height="9" viewBox="0 0 10 10"><path d="M1 5h7M5 2l3 3-3 3" stroke="#fff" stroke-width="1.4" fill="none"/></svg></span></div>
  </div>
  <div class="abs f-rule"></div>
  <div class="abs copy">© 2021 <strong>Tallowmere Cover.</strong> All Right Reserved</div>
</footer>

</body>
</html>
```